Improving the design of the attached webpage jpg image

Make the page professional, but keep it simple. All elements on the page can be changed to anything you like EXCEPT the blue bar at the top of the page.

The two images are the same page.

The content on the page must all be there. Do not add new content.

The design needs to feel like a professional score report.
Updates

Need extra days to review

Industry/Entity Type

Education

Number of Pages Required

1 page

Colors

Designer to choose colors to be used in the design.

Requirements
Must have
• The blue bar color and the bars themselves at the top and bottom of the page. All the content on the page.

```html
<!DOCTYPE html>
<html lang="en">
<head>
<meta charset="utf-8">
<title>PrepMark Admission Test Score Report</title>
<link href="https://fonts.googleapis.com/css2?family=Roboto:wght@400;500;700&family=PT+Sans:wght@400&display=swap" rel="stylesheet">
<style>
:root{
  --brand:#3e788e;
  --brand-soft:#e2edf1;
  --ink:#222a2e;
  --line:#d9e2e6;
  --track:#dde3e6;
  --white:#ffffff;
}
*{box-sizing:border-box;margin:0;padding:0}
html,body{width:746px;height:1200px;overflow:hidden;background:var(--white)}
body{font-family:'Roboto',sans-serif;color:var(--ink);position:relative}
.topbar{position:absolute;left:0;top:0;width:746px;height:57px;background:var(--brand);box-shadow:0 2px 5px rgba(0,0,0,.12);color:var(--white);font-size:16px;display:flex;align-items:center;justify-content:center}
.info-card{position:absolute;top:95px;width:215px;height:65px;background:var(--brand-soft);border-radius:10px;display:flex;align-items:center}
.info-card .icon{width:53px;height:53px;background:var(--white);border-radius:6px;margin-left:6px;display:flex;align-items:center;justify-content:center}
.info-card .label{font-weight:500;font-size:12px;line-height:18px;margin-left:17px}
.card-test{left:152px}
.card-date{left:382px}
.card-date .label{margin-left:17px}
.intro{position:absolute;top:190px;left:80px;width:586px;text-align:center;font-size:11px;line-height:16.5px}
.tab{position:absolute;top:251px;height:35px;background:var(--white);box-shadow:0 2px 6px rgba(0,0,0,.1);border-radius:3px;font-size:10px;font-weight:500;display:flex;align-items:center;justify-content:center;letter-spacing:.2px}
.tab.active{background:var(--brand);color:var(--white)}
.heading{position:absolute;left:0;width:746px;text-align:center;font-family:'PT Sans',sans-serif;font-size:29px;letter-spacing:.5px}
.heading::after{content:"";position:absolute;left:351px;bottom:-5px;width:44px;height:2px;background:var(--brand)}
.perf-table{position:absolute;left:38px;top:406px;width:673px;border-collapse:collapse}
.perf-table th{background:var(--brand-soft);height:42px;font-size:12px;font-weight:500;border:1px solid var(--line)}
.perf-table td{height:55px;border:1px solid var(--line);font-size:10px}
.perf-table .sec{text-align:left;padding-left:17px;width:209px}
.perf-table .pct{text-align:center;width:159px}
.perf-table .score{width:305px;padding:0}
.slider{display:block}
.legend-item{position:absolute;left:558px;display:flex;align-items:center;font-size:11px}
.legend-item .swatch{width:28px;height:28px;margin-right:17px}
.footer{position:absolute;left:0;top:1155px;width:746px;height:45px;background:var(--brand);color:var(--white);font-size:9px;display:flex;align-items:center;justify-content:center}
</style>
</head>
<body>
<header class="topbar">PrepMark Admission Test Score Report</header>

<div class="info-card card-test">
  <div class="icon">
    <svg width="32" height="32" viewBox="0 0 32 32" fill="none" stroke="#3e788e" stroke-width="2">
      <path d="M2 8V2h6M24 2h6v6M30 24v6h-6M8 30H2v-6"/>
      <path d="M16 7l8 4v10l-8 4-8-4V11z" fill="#3e788e"/>
      <path d="M8 11l8 4 8-4M16 15v10" stroke="#fff" stroke-width="1.2"/>
    </svg>
  </div>
  <div class="label">SIMULATION TEST 2<br>275/805</div>
</div>
<div class="info-card card-date">
  <div class="icon">
    <svg width="32" height="32" viewBox="0 0 32 32">
      <rect x="2" y="5" width="26" height="22" rx="2" fill="#3e788e"/>
      <rect x="4" y="11" width="22" height="14" fill="#fff"/>
      <g fill="#3e788e"><rect x="6" y="13" width="4" height="3"/><rect x="12" y="13" width="4" height="3"/><rect x="18" y="13" width="4" height="3"/><rect x="6" y="18" width="4" height="3"/><rect x="12" y="18" width="4" height="3"/></g>
      <g stroke="#3e788e" stroke-width="1.5"><path d="M7 2v5M12 2v5M17 2v5M22 2v5"/></g>
      <circle cx="25" cy="25" r="6.5" fill="#3e788e" stroke="#fff" stroke-width="1.5"/>
      <path d="M25 21.5V25l2.5 1.5" stroke="#fff" stroke-width="1.4" fill="none"/>
    </svg>
  </div>
  <div class="label" style="margin-left:16px">SEPTEMBER 4, 2024</div>
</div>

<p class="intro">This is text describing the test details. This is text describing the test details. This is text describing the test details. This is text describing the test details. This is text describing the test details.</p>

<nav>
  <div class="tab active" style="left:86px;width:150px">OVERALL PERFORMANCE</div>
  <div class="tab" style="left:244px;width:163px">QUANTITATIVE REASONING</div>
  <div class="tab" style="left:415px;width:133px">VERBAL REASONING</div>
  <div class="tab" style="left:556px;width:108px">DATA INSIGHTS</div>
</nav>

<h2 class="heading" style="top:340px">SECTION PERFORMANCE</h2>

<table class="perf-table">
  <tr><th class="sec">SECTION</th><th class="pct">YOUR PERCENTILE</th><th>YOUR SCORE</th></tr>
  <tr><td class="sec">Overall Performance</td><td class="pct">1th</td><td class="score">
    <svg class="slider" width="305" height="55" font-family="Roboto,sans-serif" font-size="10">
      <line x1="35" y1="30" x2="268" y2="30" stroke="#dde3e6" stroke-width="2"/>
      <circle cx="35" cy="30" r="2.5" fill="#d4dade"/><circle cx="268" cy="30" r="2.5" fill="#d4dade"/><circle cx="152" cy="30" r="2.5" fill="#d4dade"/>
      <text x="11" y="34">205</text><text x="277" y="34">805</text>
      <text x="152" y="47" text-anchor="middle">546</text>
      <circle cx="67" cy="30" r="8" fill="#3e788e"/><circle cx="67" cy="30" r="2.5" fill="#fff"/>
      <text x="67" y="16" text-anchor="middle" fill="#3e788e" font-weight="500">275</text>
    </svg></td></tr>
  <tr><td class="sec">Quantitative Reasoning</td><td class="pct">2th</td><td class="score">
    <svg class="slider" width="305" height="55" font-family="Roboto,sans-serif" font-size="10">
      <line x1="35" y1="30" x2="268" y2="30" stroke="#dde3e6" stroke-width="2"/>
      <circle cx="35" cy="30" r="2.5" fill="#d4dade"/><circle cx="268" cy="30" r="2.5" fill="#d4dade"/><circle cx="162" cy="30" r="2.5" fill="#d4dade"/>
      <text x="16" y="34">60</text><text x="277" y="34">90</text>
      <text x="162" y="47" text-anchor="middle">78</text>
      <circle cx="57" cy="30" r="8" fill="#3e788e"/><circle cx="57" cy="30" r="2.5" fill="#fff"/>
      <text x="57" y="16" text-anchor="middle" fill="#3e788e" font-weight="500">63</text>
    </svg></td></tr>
  <tr><td class="sec">Verbal Reasoning</td><td class="pct">1th</td><td class="score">
    <svg class="slider" width="305" height="55" font-family="Roboto,sans-serif" font-size="10">
      <line x1="35" y1="30" x2="268" y2="30" stroke="#dde3e6" stroke-width="2"/>
      <circle cx="35" cy="30" r="2.5" fill="#d4dade"/><circle cx="268" cy="30" r="2.5" fill="#d4dade"/><circle cx="172" cy="30" r="2.5" fill="#d4dade"/>
      <text x="16" y="34">60</text><text x="277" y="34">90</text>
      <text x="172" y="47" text-anchor="middle">79</text>
      <circle cx="67" cy="30" r="8" fill="#3e788e"/><circle cx="67" cy="30" r="2.5" fill="#fff"/>
      <text x="67" y="16" text-anchor="middle" fill="#3e788e" font-weight="500">65</text>
    </svg></td></tr>
  <tr><td class="sec">Data Insights</td><td class="pct">5th</td><td class="score">
    <svg class="slider" width="305" height="55" font-family="Roboto,sans-serif" font-size="10">
      <line x1="35" y1="30" x2="268" y2="30" stroke="#dde3e6" stroke-width="2"/>
      <circle cx="35" cy="30" r="2.5" fill="#d4dade"/><circle cx="268" cy="30" r="2.5" fill="#d4dade"/><circle cx="137" cy="30" r="2.5" fill="#d4dade"/>
      <text x="16" y="34">60</text><text x="277" y="34">90</text>
      <text x="137" y="47" text-anchor="middle">74</text>
      <circle cx="52" cy="30" r="8" fill="#3e788e"/><circle cx="52" cy="30" r="2.5" fill="#fff"/>
      <text x="52" y="16" text-anchor="middle" fill="#3e788e" font-weight="500">62</text>
    </svg></td></tr>
</table>

<h2 class="heading" style="top:721px">SCORE DISTRIBUTION</h2>

<svg class="distribution" style="position:absolute;left:0;top:780px" width="540" height="345" font-family="Roboto,sans-serif">
  <rect x="71.5" y="19.5" width="450" height="290" fill="none" stroke="#e3e9ec" stroke-width="1.5"/>
  <text transform="translate(60 157) rotate(-90)" text-anchor="middle" font-size="12" font-weight="500">LOREM IPSUM</text>
  <g font-size="9">
    <text transform="translate(113 284) rotate(-90)">Lorem ipsum dolor</text>
    <text transform="translate(125 284) rotate(-90)">consectea</text>
    <text transform="translate(197 284) rotate(-90)">Lorem ipsum dolor sit amet</text>
    <text transform="translate(209 284) rotate(-90)">consectetur</text>
    <text transform="translate(281 284) rotate(-90)">Lorem ipsum dolor</text>
    <text transform="translate(293 284) rotate(-90)">consectea</text>
    <text transform="translate(365 284) rotate(-90)">Lorem ipsum dolor sit amet</text>
    <text transform="translate(377 284) rotate(-90)">consectetur</text>
    <text transform="translate(449 284) rotate(-90)">Lorem ipsum dolor sit amet</text>
    <text transform="translate(461 284) rotate(-90)">consectetur</text>
  </g>
  <rect x="137" y="222" width="13" height="86" fill="#e2edf1"/>
  <rect x="221" y="242" width="13" height="66" fill="#3e788e"/>
  <rect x="305" y="106" width="13" height="202" fill="#e2edf1"/>
  <rect x="389" y="106" width="13" height="202" fill="#3e788e"/>
  <rect x="473" y="119" width="13" height="189" fill="#e2edf1"/>
  <rect x="276.5" y="38.5" width="187" height="54" rx="3" fill="#fff" stroke="#3e788e"/>
  <text x="370" y="62" text-anchor="middle" font-size="11">Lorem ipsum dolor sit amet,</text>
  <text x="370" y="79" text-anchor="middle" font-size="11">consectetur adipiscing</text>
  <path d="M466 99l5 13M471 112l-4-3M471 112l1-5" stroke="#3e788e" stroke-width="1.3" fill="none"/>
  <text x="315" y="335" text-anchor="middle" font-size="12" font-weight="500">LOREM IPSUM DOLOR</text>
</svg>

<div class="legend-item" style="top:903px"><span class="swatch" style="background:var(--brand)"></span>Your Score: 275</div>
<div class="legend-item" style="top:959px"><span class="swatch" style="background:var(--brand-soft)"></span>Your Percentile: 1th</div>

<footer class="footer">Copyrights © 2024 All Rights Reserved</footer>
</body>
</html>
```